Business Card Design Project

We need a business card for our new business based in Vancouver called
"Lumora Haven" We are looking for a simple yet bold design for our business cards that will enable us to stand out from the pack. All business card details will be provided in the handover stage.
Updates

Thank you to all who have submitted

The work is great for the most part
Cards with creative use of the logo
have been more successful so far

Dark cards and rounded edges 
are also getting good reviews

Double sided is an option we would like to see explored

Thank you

Target Market(s)

Our clients are stressed business people, yoga/meditation enthusiast, and people looking for a new experience in a Spa enviroment

Industry/Entity Type

Business

Font styles to use
Other font styles liked:
• please check design file

Requirements
Must have
• Lumora Haven

5218 E Kestrel Row, Vancouver, BC V5N 4K7

lumora@calmhaven.ca
Nice to have
• Creative approach to layout and design

Outside of the box design elements
Should not have
• Should not be too busy

```html
<!DOCTYPE html>
<html lang="en">
<head>
<meta charset="utf-8">
<title>Lumora Haven – Business Card</title>
<link rel="stylesheet" href="https://fonts.googleapis.com/css2?family=Didact+Gothic&display=swap">
<style>
  :root {
    --page-bg: #eef0f4;
    --card-white: #ffffff;
    --card-mist: #eceef3;
    --brand-indigo: #3b3d93;
    --brand-indigo-deep: #2c2e7c;
    --brand-indigo-light: #6b6fc0;
    --text-dark: #1f1f24;
    --text-muted: #5b5b63;
  }
  html, body {
    margin: 0;
    padding: 0;
    width: 1200px;
    height: 900px;
    overflow: hidden;
    background: var(--page-bg);
    font-family: "Didact Gothic", "Century Gothic", sans-serif;
  }
  .stage {
    width: 1200px;
    height: 900px;
    display: flex;
    align-items: center;
    justify-content: center;
  }
  .business-card {
    position: relative;
    width: 1050px;
    height: 600px;
    border-radius: 42px;
    overflow: hidden;
    background: linear-gradient(180deg, var(--card-white) 0%, var(--card-white) 55%, var(--card-mist) 100%);
    box-shadow: 0 18px 40px rgba(30, 32, 60, 0.16);
  }
  .brand-block {
    position: absolute;
    top: 82px;
    left: 0;
    right: 0;
    display: flex;
    align-items: center;
    justify-content: center;
    gap: 28px;
  }
  .brand-dot {
    width: 96px;
    height: 96px;
    border-radius: 50%;
    border: 3px solid var(--brand-indigo);
    box-sizing: border-box;
    flex: none;
  }
  .brand-name {
    margin: 0;
    font-size: 84px;
    font-weight: 400;
    line-height: 1;
    letter-spacing: 2px;
    color: var(--brand-indigo);
    white-space: nowrap;
  }
  .contact-person {
    position: absolute;
    left: 72px;
    top: 262px;
  }
  .person-name {
    margin: 0;
    font-size: 34px;
    line-height: 40px;
    font-weight: 400;
    color: var(--brand-indigo-deep);
  }
  .person-role {
    margin: 4px 0 0;
    font-size: 20px;
    line-height: 24px;
    color: var(--text-muted);
  }
  .contact-list {
    position: absolute;
    left: 72px;
    top: 372px;
    margin: 0;
    padding: 0;
    list-style: none;
    font-size: 29px;
    line-height: 40px;
    color: var(--text-dark);
    white-space: nowrap;
  }
  .contact-list .phone {
    font-size: 33px;
    margin-bottom: 4px;
  }
  .card-band {
    position: absolute;
    left: 0;
    right: 0;
    bottom: 0;
    height: 52px;
    background: linear-gradient(90deg, var(--brand-indigo-deep) 0%, var(--brand-indigo) 45%, var(--brand-indigo-light) 70%, var(--brand-indigo) 100%);
  }
</style>
</head>
<body>
  <main class="stage">
    <article class="business-card">
      <header class="brand-block">
        <div class="brand-dot" aria-hidden="true"></div>
        <h1 class="brand-name">Lumora Haven</h1>
      </header>

      <section class="contact-person">
        <p class="person-name">Elin Marwood</p>
        <p class="person-role">Manager</p>
      </section>

      <ul class="contact-list">
        <li class="phone">7604 312 918</li>
        <li class="website">www.calmhaven.ca</li>
        <li class="email">lumora@calmhaven.ca</li>
        <li class="address">5218 E Kestrel Row, Vancouver, BC V5N 4K7</li>
      </ul>

      <div class="card-band" aria-hidden="true"></div>
    </article>
  </main>
</body>
</html>
```